New Corporate website more focused on funnel and great design

Our company, Bold Harbor needs a new website to look like it's from 2021. We work with large businesses in the corporte world and need to reflect that we are professional, focused on our clients, and trsutworthy. It should include some/most of the components from our current site: boldharbor.com but should focus more about getting people to optin to out free downloads, which can be found on this page: https://www.boldharbor.com/get-started-with-a-prep-session/ and this page: https://www.boldharbor.com/team-onboarding/

Our new website should do a better job at explaining what we do, who we serve, and how we fix their problems of onboarding new leaders. Feel free to use dummy text if you are not sure what to put in for certain sections. I also would like to point out that most of the audiance is older, so we don't need anything too younge and flashy, or that is hard it use. it should have big clear fonts, plently of contrast, and work well for poeple who are not good at using the internet. Please use the colors of the logo, and you can add another color or two if you think it's fits

Industry/Entity Type

business consulting

Number of Pages Required

2 page

Font styles to use
Sans Serif

Requirements
Must have
• corporate feel, look professional, focus on getting new leads
Should not have
• cute or children feel

```html
<!DOCTYPE html>
<html lang="en">
<head>
<meta charset="utf-8">
<title>Bold Harbor – Leadership Transition Advisors</title>
<link rel="stylesheet" href="https://fonts.googleapis.com/css2?family=Montserrat:wght@400;500;600;700;800&family=Open+Sans:ital,wght@0,400;0,600;0,700;1,400&display=swap">
<style>
:root{
  --blue:#1e5fa9;
  --blue-bright:#2a7fd4;
  --navy:#123c6b;
  --footer:#1d5597;
  --ink:#1f2328;
  --text:#555b63;
  --muted:#8a9098;
  --grey-band:#f2f3f5;
  --logo-band:#e9eaec;
  --white:#fff;
}
*{margin:0;padding:0;box-sizing:border-box}
html,body{width:1200px;height:2668px;overflow:hidden;background:var(--white)}
body{position:relative;font-family:"Open Sans",Arial,sans-serif;color:var(--ink)}
.abs{position:absolute}
h1,h2,h3,.mont{font-family:"Montserrat",Arial,sans-serif}

/* hero */
.hero{left:0;top:0;width:1200px;height:600px;overflow:hidden;
  background:linear-gradient(100deg,#1a4f8f 0%,#2a5f99 35%,#7f95b3 60%,#aab9cc 80%,#5d7ea8 100%)}
.hero-bands{left:0;top:0}
.brand{left:173px;top:20px;display:flex;align-items:center;gap:10px;color:#fff}
.brand-mark{width:34px;height:34px;background:#fff}
.brand-name{font-family:"Montserrat",sans-serif;font-size:24px;font-weight:500;line-height:1}
.nav{right:174px;top:35px;display:flex;gap:20px}
.nav a{color:#fff;text-decoration:none;font-family:"Montserrat",sans-serif;font-size:10px;font-weight:700;letter-spacing:.2px}
.hero h1{left:173px;top:196px;width:520px;color:#fff;font-size:45px;line-height:49px;font-weight:400;letter-spacing:1px}
.hero h1 b{font-weight:800;letter-spacing:.5px}

.badge{width:62px;height:62px;border-radius:50%;background:#fff;box-shadow:0 3px 10px rgba(0,0,0,.12);
  display:flex;align-items:center;justify-content:center;z-index:2}
.badge i{display:block;width:22px;height:22px;background:var(--navy)}

/* intro */
.intro{left:0;top:664px;width:1200px;text-align:center;font-size:28px;line-height:32px;font-weight:600;color:var(--ink)}
.rule{width:78px;height:3px;background:var(--blue)}

/* service cards */
.svc{top:799px;width:273px;height:226px;background:#fff;box-shadow:0 2px 12px rgba(0,0,0,.1);border-bottom:4px solid var(--navy);border-radius:4px;padding:22px 18px 0 18px}
.svc h3{font-size:19px;font-weight:600;color:var(--ink)}
.svc .stat{font-family:"Montserrat",sans-serif;font-size:14px;color:#333;margin-top:9px}
.svc p{font-size:11.6px;line-height:16.6px;color:var(--text);margin-top:14px}
.svc .more{font-family:"Montserrat",sans-serif;font-size:8.5px;font-weight:700;color:var(--blue);margin-top:12px;letter-spacing:.3px}
.svc.featured{background:linear-gradient(135deg,#1c5aa3,#2e86d8);border-bottom:none}
.svc.featured h3,.svc.featured .stat,.svc.featured p,.svc.featured .more{color:#fff}

/* testimonials */
.feedback{left:0;top:1141px;width:1200px;height:476px;background:var(--grey-band)}
.globe{right:0;top:1141px;width:240px;height:440px;background:radial-gradient(ellipse at 60% 45%,#c9ccd1 0%,#dfe1e4 45%,rgba(242,243,245,0) 75%)}
.kicker{left:0;width:1200px;text-align:center;font-family:"Montserrat",sans-serif}
.quote{top:1355px;width:274px;height:187px;background:#fff;padding:45px 12px 0 12px}
.avatar{width:60px;height:60px;border-radius:50%;background:linear-gradient(160deg,#8d7f74,#4c4540);top:-30px;left:12px}
.qmark{right:16px;top:-14px;font-family:"Montserrat",sans-serif;font-size:52px;font-weight:800;color:#d4d6da;line-height:1}
.quote p{font-size:11.2px;line-height:16px;font-style:italic;color:#444;height:72px}
.quote hr{border:none;border-top:1px solid #e4e5e8;margin:10px 0 12px}
.quote .who{font-family:"Montserrat",sans-serif;font-size:12px;font-weight:600;color:var(--blue)}
.quote .role{font-family:"Montserrat",sans-serif;font-size:9px;color:#333;margin-top:2px}

/* posts */
.post{top:1804px;width:267px;height:297px;background:#fff;border:1px solid #e1e3e6;box-shadow:0 2px 10px rgba(0,0,0,.05)}
.post .img{height:184px}
.post h3{font-size:13.4px;line-height:17px;font-weight:600;margin:20px 8px 0;color:var(--ink)}
.post .by{font-size:9px;color:var(--muted);margin:11px 8px 0}
.post .read{font-family:"Montserrat",sans-serif;font-size:8.5px;font-weight:700;letter-spacing:1.6px;color:var(--blue);margin:19px 8px 0}

/* client names */
.clients{left:0;top:2206px;width:1200px;height:108px;background:var(--logo-band);display:flex;align-items:center;justify-content:space-between;padding:0 200px 0 173px}
.clients span{font-family:"Montserrat",sans-serif;font-weight:700;font-size:24px;color:#4a5058;display:flex;align-items:center;gap:8px}
.clients i{display:inline-block;width:14px;height:14px;background:#4a5058}

/* footer */
.footer{left:0;top:2313px;width:1200px;height:355px;background:var(--footer);overflow:hidden}
.skyline{left:0;bottom:0;width:1200px;height:260px;background:linear-gradient(180deg,rgba(29,85,151,0) 0%,rgba(18,60,107,.55) 100%)}
.footer h2{font-size:28px;font-weight:700;color:#fff}
.info p{font-size:14px;font-weight:600;color:#fff}
.social{display:flex;gap:6px}
.social i{width:25px;height:25px;border-radius:50%;background:#fff;display:block}
.field{background:#fff;border:1px solid #c9d3e0;font-size:10px;color:#8a9098;padding:9px 10px}
.submit{background:#111;color:#fff;font-family:"Montserrat",sans-serif;font-size:9px;font-weight:700;display:flex;align-items:center;justify-content:center;letter-spacing:.3px}
</style>
</head>
<body>

<!-- Hero -->
<section class="abs hero" role="img" aria-label="Photo of a smiling businessman in a grey suit shaking hands with a colleague in an office">
  <svg class="abs hero-bands" width="1200" height="600" viewBox="0 0 1200 600" aria-hidden="true">
    <polygon points="0,0 150,0 0,210" fill="#2f7fd0" opacity=".85"/>
    <polygon points="0,230 230,0 520,0 370,600 0,600" fill="#1b4f91" opacity=".55"/>
    <polygon points="0,380 130,600 0,600" fill="#173f74" opacity=".6"/>
  </svg>
  <div class="abs brand">
    <div class="brand-mark"></div>
    <div class="brand-name">Bold Harbor</div>
  </div>
  <nav class="abs nav">
    <a href="#">WHO WE ARE</a><a href="#">WHAT WE DO</a><a href="#">CLIENTS</a><a href="#">BLOG</a><a href="#">RESOURCES</a><a href="#">CONTACT</a>
  </nav>
  <h1 class="abs">Accelerate Business Performance <b>During Critical Leadership Transitions</b></h1>
</section>
<div class="abs badge" style="left:569px;top:569px"><i></i></div>

<!-- Intro -->
<h2 class="abs intro">Get done in 100 days what normally takes 6-12 months<br>90% of Bold Harbor clients succeed</h2>
<div class="abs rule" style="left:561px;top:754px"></div>

<!-- Services -->
<article class="abs svc" style="left:173px">
  <h3>Executive Onboarding</h3>
  <div class="stat">40% of new leaders fail</div>
  <p>For executive leaders taking on new roles, the Bold Harbor 100-Day Action Plan process prepares leaders before the start, speeds up assimilation, sets direction, builds the team, accelerates momentum, and delivers results.</p>
  <div class="more">LEARN MORE..</div>
</article>
<article class="abs svc featured" style="left:465px">
  <h3>Team Onboarding</h3>
  <div class="stat">80% of M&amp;A fail to boost returns</div>
  <p>For leaders integrating teams post acquisition or re-organization, the Bold Harbor 100 Day Action Plan process gets all players on board with the change and accelerates achievement of cultural and business integration goals.</p>
  <div class="more">LEARN MORE..</div>
</article>
<article class="abs svc" style="left:754px">
  <h3>Acceleration &amp; Restart</h3>
  <div class="stat">70% of transformations fall short</div>
  <p>For executives leading through a strategic point of inflection or reinvigorating a stalled team, Bold Harbor programs define the from-to challenge, kickstart a change process and deliver results that stick.</p>
  <div class="more">LEARN MORE..</div>
</article>

<!-- Feedback -->
<section class="abs feedback"></section>
<div class="abs globe" role="img" aria-label="Faint world globe with network connection lines"></div>
<div class="abs badge" style="left:569px;top:1113px"><i></i></div>
<div class="abs kicker" style="top:1229px;font-size:18px;color:var(--blue)">Client’s feedback is our achievement</div>
<h2 class="abs kicker" style="top:1255px;font-size:32px;font-weight:700;color:var(--ink)">Client satisfaction our goal!</h2>

<article class="abs quote" style="left:173px">
  <div class="abs avatar" role="img" aria-label="Client portrait"></div>
  <div class="abs qmark">”</div>
  <p>Somewhere right now, there is a first time CEO out there, not working with Bold Harbor, not following their 100-Day Action Plan, and I am worried for them.</p>
  <hr>
  <div class="who">Dana Whitfield</div>
  <div class="role">CEO Corvane Integrated Systems</div>
</article>
<article class="abs quote" style="left:463px">
  <div class="abs avatar" role="img" aria-label="Client portrait"></div>
  <div class="abs qmark">”</div>
  <p>Lorem ipsum dolor sit amet, consectetur adipiscing elit, sed do eiusmod tempor to incididunt ut labore et dolore magna for aliqua. Quis ipsum suspendisse.</p>
  <hr>
  <div class="who">Dana Whitfield</div>
  <div class="role">CEO Corvane Integrated Systems</div>
</article>
<article class="abs quote" style="left:754px">
  <div class="abs avatar" role="img" aria-label="Client portrait"></div>
  <div class="abs qmark">”</div>
  <p>Lorem ipsum dolor sit amet, consectetur adipiscing elit, sed do eiusmod tempor to incididunt ut labore et dolore magna for aliqua. Quis ipsum suspendisse.</p>
  <hr>
  <div class="who">Dana Whitfield</div>
  <div class="role">CEO Corvane Integrated Systems</div>
</article>

<!-- Resources -->
<div class="abs kicker" style="top:1686px;font-size:15px;font-weight:700;letter-spacing:4px;color:var(--blue)">RECENT RESOURCES</div>
<h2 class="abs kicker" style="top:1712px;font-size:32px;font-weight:700;color:var(--ink)">Featured Books and Blog Posts</h2>
<div class="abs rule" style="left:561px;top:1768px"></div>

<article class="abs post" style="left:174px">
  <div class="img" role="img" aria-label="Photo of a businesswoman talking with a colleague at a desk with a laptop" style="background:linear-gradient(135deg,#c8ced6,#6f7f94)"></div>
  <h3>When To Inform In Advance Versus Report After The Fact</h3>
  <div class="by">by Martin Hale</div>
  <div class="read">READ MORE</div>
</article>
<article class="abs post" style="left:466px">
  <div class="img" role="img" aria-label="Photo of executives seated at a hearing table" style="background:linear-gradient(135deg,#6d6f72,#2b2d31)"></div>
  <h3>Why Petrovane’s New CFO Should Fail, But Won’t</h3>
  <div class="by">by Martin Hale</div>
  <div class="read">READ MORE</div>
</article>
<article class="abs post" style="left:760px">
  <div class="img" role="img" aria-label="Photo of two smiling businesswomen in an office with a colleague behind" style="background:linear-gradient(135deg,#eceef1,#9aa7b8)"></div>
  <h3>How To Add Home Equity Through HVAC Upgrades</h3>
  <div class="by">by Martin Hale</div>
  <div class="read">READ MORE</div>
</article>

<!-- Clients -->
<section class="abs clients">
  <span><i></i>Cloudvault</span>
  <span><i></i>Northfield</span>
  <span>Ashgrove</span>
  <span>Signal TV</span>
  <span>TrueCrimson</span>
</section>

<!-- Footer -->
<footer class="abs footer">
  <div class="abs skyline" role="img" aria-label="Faint city skyline"></div>
  <div class="abs info" style="left:214px;top:32px">
    <h2>Information</h2>
    <p style="margin-top:16px">US +1 555.014.2290</p>
    <p style="margin-top:20px">UK +44 (0) 7700 900418</p>
    <div class="social" style="margin-top:20px"><i></i><i></i><i></i></div>
  </div>
  <div class="abs" style="left:566px;top:33px">
    <h2>Speak to One of Our Partners</h2>
    <div style="font-family:Montserrat,sans-serif;font-size:16px;color:#fff;margin-top:1px">Have any questions? Fire away!</div>
  </div>
  <div class="abs field" style="left:568px;top:111px;width:207px;height:30px">First Name</div>
  <div class="abs field" style="left:787px;top:111px;width:207px;height:30px">Phone</div>
  <div class="abs field" style="left:568px;top:153px;width:426px;height:30px">Email Address</div>
  <div class="abs field" style="left:568px;top:197px;width:426px;height:76px">Message</div>
  <div class="abs submit" style="left:568px;top:291px;width:118px;height:29px">SUBMIT</div>
</footer>

</body>
</html>
```